Seeking a beautiful packaging box for Dusk Haven - an essential oil blend (mock up provided!)

My sleep brand - Dusk Haven - is almost ready to go to market. And I need a box! Dusk Haven is a high end essential oils/sleep hygiene brand.

I need a gorgeous, classy box for our 3 sizes of essential oil product we are selling. I have a draft mockup which is to approximate size (attached), but need some help with the finishing touches and layout so it's really polished. I am looking for simple/monochrome designs using black and off white (think Verlin inspo!)

We are selling a 15mL dropper bottle and two roll ons (5ml, 10ml) of the essential oil blend. These are all amber bottles with black top. The box design will be almost identical for each, with very slight variations due to size differences.

The size of the boxes will be
15mL dropper: 30x30x95mm
10ml roller: 19x19x88mm
5ml roller: 18x18x59mm

Target Market(s)

High end/high price point product, shift workers, mums, people suffering stress and insomnia

Industry/Entity Type

Health And Wellness

Font styles to use
Serif
Sans Serif

Colors

Designer to choose only greyscale colors for use in the design.

Requirements
Must have
• I have attached a word document which includes all the necessary text:
- ingredients
- directions
- cautions
- info on essential oils/dusk haven (abbreviated on the smallest box)

Additionally:
- volume
- our website
- instagram logo/duskhavenau name
- made in australia
- recycle symbol
- 12 month open symbol
Nice to have
• I would like the boxes to be monochromatic: white or off white colour, with black logo and writing. I am open to variations on the logo (ie position of writing in relation to the circle/change of font size), but mostly need help with layout, font, direction of text, design of the blank spaces, patterns etc.
Should not have
• Colours

```html
<!DOCTYPE html>
<html lang="en">
<head>
<meta charset="utf-8">
<title>Dusk Haven – 15ml Box Dieline</title>
<link rel="stylesheet" href="https://fonts.googleapis.com/css2?family=Alegreya+Sans:wght@400;700&family=Marcellus&display=swap">
<style>
  :root {
    --page: #ffffff;
    --ink: #231f20;
    --panel-dark: #231f20;
    --panel-light: #ffffff;
    --text-light: #ffffff;
    --rule: #231f20;
  }
  * { box-sizing: border-box; margin: 0; padding: 0; }
  html, body {
    width: 1200px; height: 978px; overflow: hidden;
    background: var(--page);
  }
  .dieline {
    position: absolute; left: 168px; top: 144px;
    width: 852px; height: 672px;
    display: flex;
  }
  .panel {
    position: relative; width: 213px; height: 672px;
    font-family: "Alegreya Sans", sans-serif;
    font-size: 9.8px; line-height: 12px;
  }
  .panel--light { background: var(--panel-light); border: 1px solid var(--rule); color: var(--ink); }
  .panel--dark { background: var(--panel-dark); color: var(--text-light); }
  .panel b { font-weight: 700; }

  /* Ingredients */
  .ingredients { position: absolute; left: 35px; top: 280px; width: 136px; }

  /* Front */
  .brand { position: absolute; left: 0; right: 0; top: 219px; text-align: center; }
  .brand__ring {
    width: 74px; height: 74px; margin: 0 auto 22px;
    border: 2px solid var(--text-light); border-radius: 50%;
  }
  .brand__name {
    font-family: "Marcellus", serif; font-size: 44px; line-height: 44px;
    letter-spacing: 1px;
  }
  .brand__sub {
    font-family: "Marcellus", serif; font-size: 18px; line-height: 20px;
    letter-spacing: 11px; margin-top: 2px; padding-left: 11px;
  }
  .front-foot { position: absolute; left: 0; right: 0; top: 616px; text-align: center; }
  .front-foot__origin { font-size: 12px; line-height: 16px; }
  .front-foot__volume { font-size: 15px; line-height: 20px; font-weight: 700; margin-top: 3px; }

  /* Directions */
  .directions { position: absolute; left: 20px; right: 20px; top: 173px; text-align: center; }
  .directions h2 { font-size: 9.8px; font-weight: 400; margin-bottom: 13px; }
  .directions h3 { font-size: 9.8px; font-weight: 700; }
  .directions p { margin-bottom: 12px; }
  .caution { position: absolute; left: 34px; width: 150px; top: 588px; }

  /* About */
  .about { position: absolute; left: 18px; right: 18px; top: 264px; text-align: center; }
  .about p { margin-bottom: 12px; }
  .about .benefits { margin: 6px 0 22px; }
  .about .benefits li { list-style: none; margin-bottom: 7px; }
  .contact { position: absolute; left: 0; right: 0; top: 599px; text-align: center; }
  .contact__social {
    display: inline-flex; align-items: center; gap: 4px; margin-top: 12px;
  }
  .contact__dot {
    width: 10px; height: 10px; border: 1.4px solid var(--text-light); border-radius: 50%;
  }
</style>
</head>
<body>
  <main class="dieline">
    <section class="panel panel--light panel--ingredients">
      <p class="ingredients"><b>INGREDIENTS:</b> Lavandula Angustifolia (Australian Lavender), Vetiveria Zizanoides (Vetiver) Root Oil, Sweet Vanilla Fragrant Oil, Pelargonium Capitatum (Cape Rose Geranium) Leaf Extract, Juniperus Virginiana (Cedarwood) Wood Oil, Citrus Limon (Australian Lemon) Peel Oil, Origanum Majorana (Marjoram) Leaf Oil, Cananga Odorata (Ylang Ylang) Flower Oil, Anthemis Nobilis (Roman Chamomile) Flower Oil</p>
    </section>

    <section class="panel panel--dark panel--front">
      <div class="brand">
        <div class="brand__ring"></div>
        <div class="brand__name">DUSK</div>
        <div class="brand__sub">HAVEN</div>
      </div>
      <div class="front-foot">
        <div class="front-foot__origin">Made in Australia</div>
        <div class="front-foot__volume">15ml</div>
      </div>
    </section>

    <section class="panel panel--light panel--directions">
      <div class="directions">
        <h2>Directions (15mL dropper):</h2>
        <h3>Diffuse</h3>
        <p>Add 4-6 drops to a diffuser or oil burner at night to create a calm and grounded environment.</p>
        <h3>Bathe</h3>
        <p>Add 2-4 drops to a warm bath to help calm the body and mind</p>
        <h3>Inhale</h3>
        <p>Place 2 drops in the palms of the hands and inhale directly to ease you into a restful sleep</p>
        <h3>Massage</h3>
        <p>Dilute 4 drops with a carrier oil (such as jojoba or coconut), and massage into the feet before sleep</p>
      </div>
      <p class="caution"><b>Caution:</b> Possible skin sensitivity. Keep out of reach of children. Not for ingestion or internal use. Avoid contact with eyes, inner ears and sensitive areas.</p>
    </section>

    <section class="panel panel--dark panel--about">
      <div class="about">
        <p>Essential Oils have been used for centuries to help prepare the mind and body for sleep</p>
        <p>Dusk Haven contain a balanced blend of the most sleep supporting essential oils, renowned for their grounding and calming properties.</p>
        <ul class="benefits">
          <li><b>Lavender</b> for restfulness</li>
          <li><b>Vetiver</b> for grounding</li>
          <li><b>Cedarwood</b> for relaxation</li>
          <li><b>Marjoram</b> for balance</li>
          <li><b>Roman Chamomile</b> for comfort</li>
        </ul>
        <p>Add Dusk Haven to your nightly bedtime ritual to help support you in achieving deep and rejuvenating sleep</p>
      </div>
      <div class="contact">
        <div>Visit www.duskhaven.com.au<br>to learn more</div>
        <div class="contact__social"><span class="contact__dot"></span>@duskhavenau</div>
      </div>
    </section>
  </main>
</body>
</html>
```